Design an Outstanding flyer for my company.

I need a flyer designed for our window tinting company based in Brisbane Queensland Australia. The flyer will be targeting Home tinting. We also do mobile car tinting. Something in regards to this could be incorporated into the flyer as well.
I want it to be 2 sided DL size. Black background.
It really needs to Pop, and be a real attention getter.
It needs to be easy to read.
I have provided a mock up with the info on it from our marketing company. It will need a spellcheck etc to make sure everything is correct.
Everything about it can be changed however you like.
I have also included the company logo.

Lets see what you've got!

Target Market(s)

Home Owners

Industry/Entity Type

Home Improvement

Font styles to use
Other font styles liked:
• Duan Penh

Requirements
Must have
• All the information on the mock up. Clear and easy to read.
• Must Stand Out!

```html
<!DOCTYPE html>
<html lang="en">
<head>
<meta charset="utf-8">
<title>Brightline Window Tinting – DL Flyer</title>
<link href="https://fonts.googleapis.com/css2?family=Poppins:wght@300;400;600;700;800&display=swap" rel="stylesheet">
<style>
  :root {
    --backdrop: #cbcbcb;
    --black: #060606;
    --gold: #e2c62c;
    --gold-deep: #b89a1c;
    --white: #ffffff;
    --ink: #111111;
  }
  * { margin: 0; padding: 0; box-sizing: border-box; }
  html, body { width: 1200px; height: 1200px; overflow: hidden; }
  body {
    background: var(--backdrop);
    font-family: "Poppins", sans-serif;
    position: relative;
  }
  .flyer {
    position: absolute;
    top: 59px;
    width: 506px;
    height: 1067px;
    background: var(--black);
    overflow: hidden;
    box-shadow: 3px 4px 6px rgba(0,0,0,0.35);
    color: var(--white);
  }
  .flyer--front { left: 82px; }
  .flyer--back { left: 625px; }

  /* Front */
  .front-glow {
    position: absolute; inset: 0 0 auto 0; height: 460px;
    background:
      radial-gradient(circle at 70% 5%, #fffbe6 0%, #f2e7b0 12%, rgba(200,170,60,0.6) 35%, rgba(0,0,0,0) 70%),
      linear-gradient(180deg, #b9a24a 0%, #6e5d22 45%, #060606 100%);
  }
  .front-photo {
    position: absolute; left: 0; right: 0; top: 420px; height: 410px;
    background:
      linear-gradient(180deg, rgba(6,6,6,1) 0%, rgba(6,6,6,0) 25%, rgba(6,6,6,0) 70%, rgba(6,6,6,1) 100%),
      linear-gradient(90deg, #2c2b28 0%, #8c8c82 35%, #5f6b50 55%, #3a3a36 80%, #1d1d1b 100%);
  }
  .front-kicker {
    position: absolute; left: 0; right: 0; top: 107px;
    text-align: center; font-weight: 800; font-size: 32px;
    letter-spacing: 6px; color: var(--ink); line-height: 1;
  }
  .front-uv {
    position: absolute; left: 0; right: 0; top: 150px;
    text-align: center; font-weight: 700; font-size: 30px; line-height: 1;
  }
  .front-save {
    position: absolute; left: 0; right: 0; top: 200px;
    text-align: center; color: var(--gold); font-weight: 400;
    font-size: 92px; line-height: 78px;
  }
  .front-privacy {
    position: absolute; left: 0; right: 0; top: 390px;
    text-align: center; font-weight: 300; font-size: 40px; line-height: 1;
  }

  /* Brand lockup */
  .brand {
    position: absolute; left: 0; right: 0;
    display: flex; align-items: center; justify-content: center; gap: 14px;
  }
  .brand__dot {
    width: 46px; height: 46px; border-radius: 50%; background: var(--gold);
  }
  .brand__text { display: flex; flex-direction: column; align-items: flex-start; }
  .brand__name {
    font-weight: 600; font-size: 38px; line-height: 1; color: var(--gold); letter-spacing: 1px;
  }
  .brand__tag {
    font-weight: 400; font-size: 10px; letter-spacing: 10px; color: var(--gold); margin-top: 6px;
  }
  .flyer--front .brand { top: 868px; }
  .flyer--back .brand { top: 862px; }

  .web {
    position: absolute; left: 0; right: 0; text-align: center;
    font-size: 16px; letter-spacing: 3px; color: var(--white);
  }
  .web span { color: var(--gold); }
  .flyer--front .web { top: 974px; }
  .flyer--back .web { top: 968px; }

  /* Back */
  .back-photo {
    position: absolute; left: 163px; top: 0; width: 343px; height: 200px;
    background: linear-gradient(180deg, #7a8fa8 0%, #b9b2a0 45%, #6e6a60 75%, #060606 100%);
  }
  .back-fade {
    position: absolute; left: 0; right: 0; top: 150px; height: 80px;
    background: linear-gradient(180deg, rgba(6,6,6,0), var(--black));
  }
  .badge { position: absolute; left: 0; top: 0; }
  .back-title {
    position: absolute; right: 58px; top: 150px; text-align: right;
  }
  .back-title__count { font-size: 84px; line-height: 72px; font-weight: 400; }
  .back-title__reasons { font-size: 31px; font-weight: 400; }
  .back-title__rest { font-size: 33px; line-height: 38px; font-weight: 400; }
  .reasons {
    position: absolute; right: 58px; top: 302px; list-style: none; text-align: right;
    font-size: 19px; font-weight: 300; line-height: 24.3px;
  }
  .reasons li:nth-child(odd) { color: var(--gold); }
  .back-sheen {
    position: absolute; left: 0; right: 0; top: 640px; height: 260px;
    background: linear-gradient(160deg, rgba(6,6,6,0) 20%, rgba(120,110,80,0.35) 50%, rgba(6,6,6,0) 80%);
  }
  .call {
    position: absolute; left: 0; right: 0; top: 712px; text-align: center;
    font-weight: 800; font-size: 23px; line-height: 25px;
  }
  .contact {
    position: absolute; left: 0; right: 0; top: 776px; text-align: center;
    font-weight: 800; font-size: 25px; line-height: 32px; color: var(--gold);
  }
</style>
</head>
<body>

<section class="flyer flyer--front">
  <div class="front-glow"></div>
  <div class="front-photo" role="img" aria-label="Bright open-plan living room with tinted sliding glass doors looking out to a garden"></div>
  <p class="front-kicker">Keep Heat Out</p>
  <p class="front-uv">Block 99.9% UV Rays</p>
  <h1 class="front-save">Save<br>Money</h1>
  <p class="front-privacy">Increase Privacy</p>
  <div class="brand">
    <span class="brand__dot"></span>
    <div class="brand__text">
      <span class="brand__name">BRIGHTLINE</span>
      <span class="brand__tag">WINDOW TINTING</span>
    </div>
  </div>
  <p class="web">www.<span>brightlinetinting</span>.com.au</p>
</section>

<section class="flyer flyer--back">
  <div class="back-photo" role="img" aria-label="View through a tinted home window to a fence and tiled rooftops"></div>
  <div class="back-fade"></div>
  <svg class="badge" width="172" height="236" viewBox="0 0 172 236" aria-label="Car window tinting also available. Contact us for a quote.">
    <path d="M0 0 H168 A168 168 0 0 1 0 236 Z" fill="#e2c62c"/>
    <g transform="translate(88 110) rotate(-42)" font-family="Poppins, sans-serif" font-weight="600" font-size="15" fill="#111" text-anchor="middle">
      <text y="-34">Car Window</text>
      <text y="-16">Tinting</text>
      <text y="2">also available.</text>
      <text y="20">Contact us</text>
      <text y="38">for a quote.</text>
    </g>
  </svg>
  <div class="back-title">
    <div><span class="back-title__count">20</span><span class="back-title__reasons">Reasons</span></div>
    <div class="back-title__rest">Why Home Window<br>Tinting is Perfect for You</div>
  </div>
  <ul class="reasons">
    <li>Reduce Glare</li>
    <li>Reduce Energy Costs</li>
    <li>Control Amount Of Light Entering Home</li>
    <li>Reduce Carbon Footprint</li>
    <li>Make Home More Beautiful</li>
    <li>Eliminate Home Hot Spots</li>
    <li>Protect Against Broken Glass</li>
    <li>Regulate Energy</li>
    <li>Protect Upholstery</li>
    <li>Improve Effectiveness Of Roof Insulation</li>
    <li>Improve Health</li>
    <li>Reduce Interior Floor Fading</li>
    <li>Eliminate Need For Blinds</li>
    <li>Strengthen Your Windows</li>
    <li>Insulate In Winter</li>
    <li>Affordable</li>
  </ul>
  <div class="back-sheen"></div>
  <p class="call">Call Brisbane’s Leader in<br>Home Window Tinting Today</p>
  <p class="contact">Tel: 07 3000 1234<br>SMS: 0400 000 123</p>
  <div class="brand">
    <span class="brand__dot"></span>
    <div class="brand__text">
      <span class="brand__name">BRIGHTLINE</span>
      <span class="brand__tag">WINDOW TINTING</span>
    </div>
  </div>
  <p class="web">www.<span>brightlinetinting</span>.com.au</p>
</section>

</body>
</html>
```